BVX2014 Brochure

TRQN needs a design for a brochure cover and inside page for our annual users' conference to take place in January 2014. Every year, we host a popular users group meeting where 800 - 1,000 of our customers attend a 3-day meeting in Houston TX to learn how to more effectively use our software, network with industry peers, and provide feedback on future changes to the software. The goal of the brochure is to get our customers excited about next year's BVXs, and to sell out the events. (An example of last year's brochure is attached. We are not necessarily looking for something similar. It's just to give you an idea of what kind of content is in the brochure.)

The name of the event is 2014 Client Field Summit (also known as BVX).

Theme - the theme of this year's meeting is "Where Innovative Software Meets Real-World Application."

Over 90% of our market are males. They are mainly C-level or managers in construction companies. Our software includes estimating, field entry and reporting, dispatching and scheduling, equipment maintenance management, fuel management, safety management, GPS tracking, and mobile apps. Our corporate color is green, specifically PMS356.

TRQN Brand personality traits - Innovative, market leader, competent, professional, masculine, friendly, and helpful. We've been in business for 28 years, and we are known for our world-class customer support and friendly helpful employees.

Target Market(s)

Construction company executives, estimators, project managers, equipment managers, and IT support. 90% male. We mainly target US and Canadian customers.

Industry/Entity Type

Group

Requirements
Must have
• It needs to be very clear (i.e. probably larger) that this is our 2014 Client Field Summit, and the theme of this year's meeting "Where Innovative Software Meets Real-World Application" needs to be prominent. The meeting name, theme, and our company logo should be prominent.
• Brochure title - 2014 Client Field Summits
• Location - Houston, TX
• Dates - Jan 29 - 31 and Feb 20 - 22 (we host the same meeting twice, but have 1 brochure and registration site)
• Theme - Where Innovative Software Meets Real-World Application
• Logo - we want our logo (TRQN Bold Tools for the Building Trades) to be prominent & should not be altered from the attached image
• Register Today! call to action pointing people to our registration site at www.trqn-example.com/BVX
• Colors - We want our green (PMS 356) to be the dominant color
• Pictures - we want at least 1 picture from past events showing that the meetings are popular, helpful, collaborative and fun.
• Company info on back cover - TRQN, 48207 E. Pelham Rd. Marlow Creek, TX 77592, 800-555-0147, www.trqn-example.com
Nice to have
• When customers view the brochure, we want them to get the following feelings:
• - Professional meeting
• - Innovative technologies
• - New mobile applications on tablets and smartphones
• - Helpful, where they can learn tips and best practices
• - Fun
• Even if they don't attend the meeting, we want everyone who receives the brochure to get a positive feeling about our company.
Should not have
• Feminine design - our industry is largely male construction professionals.
• Don't use script or other goofy fonts
• Logo that is so small it is unreadable
• Too much text
• A design that doesn't project a professional or innovative image

```html
<!DOCTYPE html>
<html lang="en">
<head>
<meta charset="utf-8">
<title>BVX2014 Brochure – Inner Spread</title>
<link rel="stylesheet" href="https://fonts.googleapis.com/css2?family=Roboto+Slab:wght@700&family=PT+Sans:wght@400;700&display=swap">
<style>
:root{
  --green:#11893b;
  --green-dark:#0b6d2e;
  --yellow:#f9b91c;
  --orange:#f39a1f;
  --ink:#2f2f2f;
  --paper:#f4f4f4;
  --stage:#e6e6e6;
  --photo-warm:#7a5a45;
  --photo-cool:#8f969c;
  --slab:"Roboto Slab","Rockwell",serif;
}
*{margin:0;padding:0;box-sizing:border-box}
html,body{width:1200px;height:1000px;overflow:hidden;background:var(--stage)}
body{font-family:"PT Sans",sans-serif;color:var(--ink);position:relative}
.spread{position:absolute;left:48px;top:22px;width:1105px;height:816px;display:flex;box-shadow:0 2px 10px rgba(0,0,0,.25)}
.page{position:relative;height:100%;overflow:hidden;background:linear-gradient(180deg,#fff 0%,var(--paper) 100%)}
.page-left{width:550px;border-right:1px solid #d6d6d6}
.page-right{width:555px}
.abs{position:absolute}
svg.abs{display:block}

/* left */
.theme-title{left:36px;top:98px;font-family:var(--slab);font-weight:700;font-size:19px;line-height:24px;color:#222}
.intro{left:36px;top:168px;width:452px;font-size:13.5px;line-height:21px}
.agenda-box{left:22px;top:338px;width:500px;height:252px;background:var(--green);border-radius:12px}
.agenda-tab{left:22px;top:304px}
.agenda-title{left:36px;top:318px;font-family:var(--slab);font-weight:700;font-size:17px;line-height:22px;color:var(--green-dark)}
.agenda-list{left:36px;top:352px;list-style:none;color:#fff;font-size:13.5px;line-height:21.2px}
.agenda-list li{display:flex}
.agenda-list .time{width:157px;white-space:pre}
.quote-mark{font-family:var(--slab);font-size:90px;color:#9a9a9a;line-height:1}
.quote{left:308px;top:668px;width:220px;font-size:14.5px;line-height:21px}
.quote-by{left:343px;top:754px;font-size:12.5px;line-height:20px}

/* right */
.session-head{left:22px;height:40px}
.session-head .tab{position:absolute;left:0;top:0;height:100%;background:var(--yellow);font-family:var(--slab);font-weight:700;color:#222;font-size:16px;line-height:20px;padding:3px 6px;z-index:1}
.session-head .band{position:absolute;top:6px;height:28px;background:var(--green);color:#fff;font-family:var(--slab);font-weight:700;font-size:15px;line-height:28px;padding-left:18px}
.tab small{display:block;font-family:"PT Sans",sans-serif;font-weight:400;font-size:10px;line-height:10px;text-align:center}
.session-title{left:27px;font-weight:700;font-size:15px;line-height:20px;color:#222}
.track{left:27px;font-weight:700;font-size:15px;line-height:20px;color:var(--green)}
.session-text{left:27px;width:245px;font-size:13.5px;line-height:22px}
.bullets{left:27px;list-style:none;font-size:13.5px}
.bullets li{position:relative;padding-left:22px}
.bullets li::before{content:"";position:absolute;left:2px;top:6px;width:8px;height:8px;background:var(--orange);transform:rotate(45deg)}
.bullets-tight{line-height:18.5px}
.bullets-tight li{margin-bottom:4px}
.bullets-tight li.narrow{width:310px}
.bullets-open{line-height:22.5px}
.promo{left:35px;top:642px;font-size:15px;line-height:20px}
.promo strong{font-family:var(--slab);font-size:15.5px}
.promo .stat{color:var(--green);font-weight:700}
.register{left:388px;top:704px;width:128px;height:82px;background:#2b2b2b;border:3px solid #cfcfcf;border-radius:8px;color:#fff;text-align:center}
.register b{display:block;font-size:22px;line-height:24px;margin-top:4px}
.register span{display:block;font-size:9px;margin-top:8px;font-weight:700}
</style>
</head>
<body>
<div class="spread">

  <section class="page page-left">
    <svg class="abs" style="left:0;top:0" width="550" height="100" viewBox="0 0 550 100">
      <path d="M0 0H550V58Q300 70 0 86Z" fill="var(--photo-warm)" role="img" aria-label="Photo of a crowded conference hall full of attendees"/>
      <path d="M0 86Q300 70 550 58V68Q300 80 0 96Z" fill="var(--green)"/>
      <path d="M0 96Q300 80 550 68V72Q300 84 0 100Z" fill="var(--yellow)"/>
    </svg>

    <h1 class="abs theme-title">Where Innovative Software Meets<br>Real-World Application</h1>
    <p class="abs intro">Iriliquis accum nonsenit augait ad magna consequam in vel dolorem dolor adiat irilla feu faccum velit vel dolor ad delent nons atetum zzrit la faccum dolobortis alisi.<br>Uptat. Ibh erat vel ex ero commy nim do odio odolorp ercipsum autem acincidunt at alit num ad ea faciliquisl dipit nulluptat</p>

    <div class="abs agenda-box"></div>
    <svg class="abs agenda-tab" width="260" height="48" viewBox="0 0 260 48">
      <path d="M0 0H212L232 24L212 44H0Z" fill="var(--green)"/>
      <path d="M0 8H208L228 44H0Z" fill="var(--yellow)"/>
    </svg>
    <h2 class="abs agenda-title">Agenda : Thursday</h2>
    <ul class="abs agenda-list">
      <li><span class="time">7:00 am   –  8:00 am</span>Registration &amp; Continental Breakfast</li>
      <li><span class="time">8:00 am   –  8:45 am</span>Opening Keynote</li>
      <li><span class="time">9:00 am   –  10:15 am</span>Classes, Session 1</li>
      <li><span class="time">10:15 am –  10:30 am</span>Break</li>
      <li><span class="time">10:30 am –  11:45 am</span>Classes, Session 2</li>
      <li><span class="time">11:45 am –  1:00 pm</span>Lunch</li>
      <li><span class="time">1:00 pm   –  2:15 pm</span>Classes, Session 3</li>
      <li><span class="time">2:15 pm   –  2:30 pm</span>Break</li>
      <li><span class="time">2:30 pm   –  3:45 pm</span>Classes, Session 4</li>
      <li><span class="time">4:00 pm   –  6:00 pm</span>Welcome Reception &amp; Coaches' Corner</li>
      <li><span class="time">5:30 pm   –  6:00 pm</span>Honoree Reception, Invitation only</li>
    </ul>
    <svg class="abs" style="left:362px;top:372px" width="160" height="164" viewBox="0 0 160 164">
      <ellipse cx="80" cy="82" rx="76" ry="78" fill="var(--orange)"/>
      <ellipse cx="80" cy="82" rx="70" ry="72" fill="var(--photo-cool)" role="img" aria-label="Photo of attendees seated at round tables in a session hall"/>
    </svg>

    <svg class="abs" style="left:0;top:596px" width="550" height="220" viewBox="0 0 550 220">
      <path d="M0 18Q200 10 300 130V220H0Z" fill="var(--photo-cool)" role="img" aria-label="Photo of attendees working on laptops during a class"/>
      <path d="M0 4Q210 -4 312 130L302 130Q200 8 0 14Z" fill="var(--green)"/>
      <path d="M0 14Q200 8 302 130L298 132Q198 14 0 20Z" fill="var(--yellow)"/>
    </svg>
    <span class="abs quote-mark" style="left:262px;top:640px">“</span>
    <p class="abs quote">Great way to learn about new features and network with other contractors on how they are solving problems.</p>
    <p class="abs quote-by">-Dale Korwin, Project Manager<br>&nbsp;The Varnell Group</p>
    <span class="abs quote-mark" style="left:502px;top:736px">”</span>
  </section>

  <section class="page page-right">
    <svg class="abs" style="left:270px;top:0" width="285" height="190" viewBox="0 0 285 190">
      <path d="M14 0H285V178Q150 192 80 130Q20 80 14 0Z" fill="var(--photo-cool)" role="img" aria-label="Photo of a construction worker with a tablet at a highway bridge site"/>
      <path d="M14 0Q20 80 80 130Q150 192 285 178V185Q145 200 74 135Q10 82 6 0Z" fill="var(--green)"/>
    </svg>

    <div class="abs session-head" style="top:14px">
      <div class="band" style="left:86px;width:180px">9.00 am - 3.45 pm</div>
      <div class="tab" style="width:94px">Thursday<small>(all day)</small></div>
    </div>
    <h3 class="abs session-title" style="top:59px">Cost Entry Bootcamp</h3>
    <p class="abs track" style="top:78px">Estimating</p>
    <p class="abs session-text" style="top:100px">One-day crash course in cost entry for estimators not very familiar withTallyBid.</p>
    <ul class="abs bullets bullets-tight" style="top:147px;width:430px">
      <li class="narrow">Introduction to essential key concepts, such as cture, resource coding, use of master estimates, estimate-specific data vs. system-wide data.</li>
      <li>How to stick-build activities.</li>
      <li>Use and modification of crews during cost entry.</li>
      <li>Copying biditems/activities from other estimateas.</li>
      <li>Importing activities from the activity codebook into an estimate.</li>
      <li>Use of Quick Sub/Material Entry feature to add subs to a bid.</li>
      <li>Basic use of Quote Management system to handle quotes.</li>
      <li>Basic use of the Bid Summary screen to add and spread costs.</li>
    </ul>

    <div class="abs session-head" style="top:368px">
      <div class="band" style="left:86px;width:446px">9.00 am - 10.15 am</div>
      <div class="tab" style="width:94px;height:30px;top:4px;line-height:24px">Thursday</div>
    </div>
    <h3 class="abs session-title" style="top:410px">Use the Quote System to Effectively Manage Quotes - Part 1</h3>
    <p class="abs track" style="top:429px">Estimating</p>
    <ul class="abs bullets bullets-open" style="top:453px;width:450px">
      <li>Prepare, organize and update pricing for sub and material vendors.</li>
      <li>Understand the importance of estimate entry on efficient use of the Quote System.</li>
      <li>Review how the Quote System relates to bid closing.</li>
      <li>Understand how vendor setup affects the Quote System.</li>
      <li>Be familiar with all of the time-saving automation features.</li>
      <li>Be able to choose which automation features are appropriate for your company.</li>
    </ul>

    <svg class="abs" style="left:0;top:610px" width="555" height="206" viewBox="0 0 555 206">
      <path d="M0 206Q300 200 555 40V206Z" fill="#fff"/>
      <path d="M0 196Q300 186 555 30V46Q300 196 0 204Z" fill="var(--green)"/>
      <path d="M0 204Q300 196 555 46V54Q300 202 0 210Z" fill="var(--yellow)"/>
      <rect x="318" y="50" width="180" height="128" rx="8" fill="var(--photo-cool)" role="img" aria-label="Illustration of a laptop showing the event registration web page"/>
      <circle cx="56" cy="148" r="33" fill="var(--yellow)"/>
      <circle cx="56" cy="148" r="28" fill="var(--green)" role="img" aria-label="Tip lightbulb icon"/>
    </svg>
    <p class="abs promo"><strong>Bring two people<br>so you can cover more classes.</strong><br><span class="stat">69 %</span> of companies in 2012<br>brought more than 1 attendee</p>
    <div class="abs register"><b>Register<br>Online!</b><span>www.trqn-example.com/BVX</span></div>
  </section>

</div>
</body>
</html>
```